For Lease sign for Property management company in Kansas City

We need someone to take our information and design a standard for lease sign that we can put in front of each of our buildings. I would love for it to do its job of letting people know there are units available but also be unique somehow. Also the aspect ratio of the design would ideally be 4 wide by 3 tall but we open to other ideas. It will be a larger yard sign.

Target Market(s)

Potential Tenants

Industry/Entity Type

Real Estate Development

Font styles to use
Sans Serif

Requirements
Must have
• Our logo, our website (www.tollen-estates.com), our phone number (816) 247-5903.
Nice to have
• Some how say "For Lease"
Sign to be 4' wide by 3' tall
If there was a place to put the building name that would be cool but not ne
Should not have
• Nothing that I can think of

```html
<!DOCTYPE html>
<html lang="en">
<head>
<meta charset="utf-8">
<title>For Lease Yard Sign – Tollen Estates</title>
<link href="https://fonts.googleapis.com/css2?family=Jost:wght@500;600;700&display=swap" rel="stylesheet">
<style>
  :root {
    --sign-red: #be1e2d;
    --sign-gold: #fbb040;
    --sign-white: #ffffff;
    --ink-black: #111111;
    --ink-grey: #58595b;
    --page-bg: #ecebe8;
  }
  * { margin: 0; padding: 0; box-sizing: border-box; }
  html, body {
    width: 728px;
    height: 1200px;
    overflow: hidden;
    background: var(--page-bg);
    font-family: "Jost", "Futura", sans-serif;
  }
  .lease-sign {
    position: absolute;
    left: 24px;
    top: 345px;
    width: 680px;
    height: 510px;
    background: var(--sign-white);
    box-shadow: 10px 14px 22px rgba(0, 0, 0, 0.35);
    overflow: hidden;
  }
  .headline-panel {
    position: absolute;
    left: 0;
    top: 0;
    width: 383px;
    height: 100%;
    background: var(--sign-red);
  }
  .headline {
    position: absolute;
    left: 38px;
    top: 34px;
    color: var(--sign-white);
    font-weight: 700;
    font-size: 106px;
    line-height: 0.98;
    letter-spacing: 1px;
  }
  .contact-band {
    position: absolute;
    left: 0;
    top: 349px;
    width: 383px;
    height: 130px;
    background: var(--sign-gold);
    padding: 28px 0 0 38px;
    color: var(--ink-black);
  }
  .contact-phone {
    font-weight: 700;
    font-size: 41px;
    line-height: 1;
    letter-spacing: 0.5px;
  }
  .contact-web {
    font-weight: 700;
    font-size: 19px;
    line-height: 1.3;
    margin-top: 2px;
  }
  .brand-panel {
    position: absolute;
    left: 383px;
    top: 0;
    width: 297px;
    height: 100%;
    display: flex;
    flex-direction: column;
    align-items: center;
  }
  .brand-dot {
    margin-top: 52px;
    width: 102px;
    height: 102px;
    border-radius: 50%;
    background: var(--sign-gold);
  }
  .brand-name {
    margin-top: 20px;
    color: var(--sign-red);
    font-weight: 700;
    font-size: 40px;
    line-height: 1;
    text-align: center;
    letter-spacing: 1px;
  }
  .building-name {
    position: absolute;
    top: 395px;
    width: 100%;
    text-align: center;
    color: var(--ink-grey);
    font-weight: 500;
    font-size: 27px;
    letter-spacing: 0.5px;
  }
</style>
</head>
<body>
  <div class="lease-sign">
    <div class="headline-panel">
      <h1 class="headline">FOR<br>LEASE</h1>
      <div class="contact-band">
        <p class="contact-phone">(816) 247-5903</p>
        <p class="contact-web">www.tollen-estates.com</p>
      </div>
    </div>
    <div class="brand-panel">
      <div class="brand-dot"></div>
      <p class="brand-name">TOLLEN<br>ESTATES</p>
      <p class="building-name">BUILDING NAME</p>
    </div>
  </div>
</body>
</html>
```